Harborline Stay Collective Business Card Design

Design a business card for Harborline Stay Collective. Look at the website for colors and reference. Card should have logo, name, title, office number, mobile number, email, URL and a tagline like, "Luxury Hotel & Resort Email Marketing" (This might change).

https://www.harborlinestaycollective.net

The rest I will leave up to your imagination.

Contact Information for Business Card

Logo, name, title, office number, mobile number, email, URL and a tagline like, "Luxury Hotel & Resort Email Marketing" (This might change).

```html
<!DOCTYPE html>
<html lang="en">
<head>
<meta charset="utf-8">
<title>Harborline Stay Collective – Business Card</title>
<link href="https://fonts.googleapis.com/css2?family=Montserrat:wght@400;500;600;700&display=swap" rel="stylesheet">
<style>
  :root {
    --orange: #f07a10;
    --ink: #1b1b1b;
    --grey: #6d6d6d;
    --white: #ffffff;
    --backdrop: #e9e9e9;
    --sky: #5b86b8;
    --forest: #4d6a34;
    --sea: #1f9aa0;
  }
  * { margin: 0; padding: 0; box-sizing: border-box; }
  html, body {
    width: 1200px; height: 987px; overflow: hidden;
    background: var(--backdrop);
    font-family: "Montserrat", sans-serif;
  }
  .sheet {
    width: 1200px; height: 987px;
    display: flex; flex-direction: column; align-items: center; justify-content: center;
    gap: 48px;
  }
  .card {
    width: 700px; height: 400px;
    position: relative; overflow: hidden;
    box-shadow: 0 6px 18px rgba(0,0,0,.18);
    background: var(--white);
  }
  /* Front */
  .card-front__photo {
    position: absolute; inset: 0 0 62px 0;
    background: linear-gradient(180deg, var(--sky) 0%, #7c9a6a 30%, var(--forest) 52%, #2c8c8e 72%, var(--sea) 100%);
  }
  .card-front__brand {
    position: absolute; left: 0; right: 0; top: 130px;
    text-align: center;
    display: flex; align-items: center; justify-content: center; gap: 14px;
  }
  .card-front__brand .brand-name {
    color: var(--white); font-weight: 700; font-size: 38px; letter-spacing: 1px; text-transform: uppercase;
  }
  .brand-mark { width: 22px; height: 22px; background: var(--orange); flex: none; }
  .card-front__band {
    position: absolute; left: 0; right: 0; bottom: 0; height: 62px;
    background: var(--orange);
    display: flex; align-items: center; justify-content: center;
  }
  .tagline { color: var(--white); font-weight: 500; font-size: 20px; letter-spacing: .5px; }

  /* Back */
  .card-back__brand {
    position: absolute; left: 44px; top: 168px; width: 300px;
    display: flex; align-items: center; gap: 12px;
  }
  .card-back__brand .brand-name {
    color: var(--ink); font-weight: 700; font-size: 24px; line-height: 1.15; text-transform: uppercase; letter-spacing: .5px;
  }
  .card-back__divider {
    position: absolute; left: 360px; top: 90px; width: 2px; height: 220px; background: var(--orange);
  }
  .card-back__details { position: absolute; left: 386px; top: 96px; }
  .person-name { font-weight: 600; font-size: 28px; color: var(--ink); }
  .person-title { font-weight: 500; font-size: 18px; color: var(--grey); margin-top: 2px; }
  .contact-list { list-style: none; margin-top: 24px; }
  .contact-list li {
    display: flex; align-items: center; gap: 10px;
    font-size: 17px; color: var(--grey); line-height: 1.6;
  }
  .contact-list svg { width: 15px; height: 15px; flex: none; fill: none; stroke: var(--orange); stroke-width: 2; }
</style>
</head>
<body>
<main class="sheet">
  <section class="card card-front">
    <div class="card-front__photo" role="img" aria-label="Photograph of a rocky, tree-covered coastal headland above turquoise surf"></div>
    <div class="card-front__brand">
      <span class="brand-mark"></span>
      <span class="brand-name">Harborline Stay Collective</span>
    </div>
    <div class="card-front__band"><p class="tagline">Luxury Hotel &amp; Resort Email Marketing</p></div>
  </section>

  <section class="card card-back">
    <div class="card-back__brand">
      <span class="brand-mark"></span>
      <span class="brand-name">Harborline Stay Collective</span>
    </div>
    <div class="card-back__divider"></div>
    <div class="card-back__details">
      <h1 class="person-name">Daniel Reyes</h1>
      <p class="person-title">President</p>
      <ul class="contact-list">
        <li><svg viewBox="0 0 16 16"><path d="M3 2l3 1 1 3-2 1a8 8 0 004 4l1-2 3 1 1 3-2 1C7 14 2 9 2 4z"/></svg>014-555-2718</li>
        <li><svg viewBox="0 0 16 16"><rect x="4" y="1.5" width="8" height="13" rx="1.5"/><line x1="7" y1="12" x2="9" y2="12"/></svg>014-555-2719</li>
        <li><svg viewBox="0 0 16 16"><rect x="1.5" y="3.5" width="13" height="9"/><path d="M1.5 3.5l6.5 5 6.5-5"/></svg>info@harborlinestaycollective.net</li>
        <li><svg viewBox="0 0 16 16"><circle cx="8" cy="8" r="6.5"/><ellipse cx="8" cy="8" rx="3" ry="6.5"/><line x1="1.5" y1="8" x2="14.5" y2="8"/></svg>harborlinestaycollective.net</li>
      </ul>
    </div>
  </section>
</main>
</body>
</html>
```